A book about police officer shootings needs a dynamic cover design

I've almost completed a book on officer involved shootings...a very hot topic today. The title is "R.K.V. Beyond The Silence Broke." (emphasis on "Beyond The Silence") It details three separate shooting incidents, all within the same law enforcement family.I need a professional looking book cover that helps capture the drama. I attached a file of something I put together that is close, but I am concerned about "readability" and want a more professional look. I included a photo that I took off the internet of a gun being shot. That particular photo can stay or go, or be altered, but I like the perspective of the photo being fired from the person behind it. I wanted the cover to have the characteristics and color of a police uniform, utilizing blues, silvers, and maybe a little gold. I'm concerned about making sure the font and colors are also easy to read. I also will be working on a website design for "Beyond The Silence.Com" once the book hits the market. The back cover will incorporate the same colors, but only be a picture and excerpts from the book. I've included both for your review.

Target Market(s)

Law Enforcement, Christian, Media

Font styles to use
Sans Serif

Requirements
Must have
• A professional and readable appearance, that captures the drama of the topic. All the wording on the sample cover I attached, unless you come up with something better. A gun being fired from the perspective of the officer pulling the trigger. The size of the book will be the standard 6 x 9 in size. "Beyond The Silence" will eventually be my website domain and social media promotion hashtag.
Nice to have
• I would like the cover to incorporate the colors of a police uniform and badge, traditionally, navy blue, silver and some gold.
Should not have
• No police badge with a black band across. Not my topic.

```html
<!DOCTYPE html>
<html lang="en">
<head>
<meta charset="UTF-8">
<title>R.K.V. Beyond The Silence Broke – Cover Spread</title>
<link rel="stylesheet" href="https://fonts.googleapis.com/css2?family=Archivo:wght@700;800;900&family=Archivo+Black&family=Roboto+Condensed:wght@700&display=swap">
<style>
  :root {
    --navy-deep: #0b2f5c;
    --navy: #124477;
    --navy-light: #2a679f;
    --spine: #0e3767;
    --silver-hi: #ffffff;
    --silver-mid: #b8c6d6;
    --silver-lo: #7f93ab;
    --text-soft: #c9d6e6;
    --heading: #a9bdd4;
    --rule: #5d86b3;
  }
  * { margin: 0; padding: 0; box-sizing: border-box; }
  html, body { width: 1200px; height: 800px; overflow: hidden; background: var(--navy-deep); }
  body { font-family: "Archivo", Arial, sans-serif; }

  .cover-spread {
    position: relative;
    width: 1200px; height: 800px;
    background: radial-gradient(ellipse at 75% 55%, var(--navy-light) 0%, var(--navy) 45%, var(--navy-deep) 100%);
    overflow: hidden;
  }

  /* Back cover */
  .back-cover { position: absolute; left: 0; top: 0; width: 574px; height: 800px; }
  .back-quote {
    position: absolute; top: 44px; left: 0; width: 574px; text-align: center;
    font-weight: 800; font-size: 14px; color: var(--text-soft); white-space: nowrap;
  }
  .family-photo {
    position: absolute; left: 152px; top: 70px; width: 270px; height: 310px;
    background: linear-gradient(180deg, #8fb0d3 0%, #5d7fa6 30%, #2b4a72 70%, #1c3557 100%);
  }
  .photo-captions {
    position: absolute; top: 388px; left: 0; width: 574px; height: 14px;
    font-weight: 800; font-size: 10.5px; color: var(--text-soft);
  }
  .photo-captions span { position: absolute; top: 0; transform: translateX(-50%); white-space: nowrap; }
  .caption-left { left: 198px; }
  .caption-mid { left: 290px; }
  .caption-right { left: 380px; }

  .excerpt { position: absolute; left: 56px; width: 458px; }
  .excerpt h3 { font-weight: 800; font-size: 15px; color: var(--heading); margin-bottom: 2px; }
  .excerpt p { font-weight: 700; font-size: 11.2px; line-height: 15.2px; color: var(--text-soft); }
  .excerpt-one { top: 411px; }
  .excerpt-two { top: 506px; }
  .excerpt-three { top: 616px; }

  /* Spine */
  .spine {
    position: absolute; left: 574px; top: 0; width: 54px; height: 800px;
    background: linear-gradient(180deg, var(--spine), #0a2c55);
    border-left: 1px solid var(--rule); border-right: 1px solid var(--rule);
  }
  .spine-text {
    position: absolute; left: 0; top: 66px; width: 52px; height: 680px;
    writing-mode: vertical-rl; transform: rotate(180deg);
    display: flex; align-items: center; justify-content: flex-start; gap: 34px;
    white-space: nowrap;
  }
  .spine-author { font-family: "Archivo Black", Arial, sans-serif; font-size: 27px; letter-spacing: 1px; color: var(--silver-mid); }
  .spine-title { font-family: "Archivo Black", Arial, sans-serif; font-size: 34px; color: var(--silver-hi); }
  .spine-subtitle { font-weight: 800; font-size: 20px; color: var(--silver-mid); }

  /* Front cover */
  .front-cover { position: absolute; left: 628px; top: 0; width: 572px; height: 800px; }
  .firing-scene {
    position: absolute; left: 0; top: 0; width: 572px; height: 800px;
    background: radial-gradient(circle 280px at 68% 60%, rgba(150,190,230,0.5) 0%, rgba(70,120,180,0.3) 45%, rgba(18,68,119,0) 100%);
  }
  .front-tagline {
    position: absolute; top: 38px; left: 0; width: 572px; text-align: center;
    font-family: "Roboto Condensed", Arial, sans-serif; font-weight: 700; font-size: 22px; color: var(--text-soft);
    white-space: nowrap;
  }
  .silver-text {
    background: linear-gradient(180deg, var(--silver-hi) 0%, var(--silver-mid) 50%, var(--silver-lo) 100%);
    -webkit-background-clip: text; background-clip: text; color: transparent;
  }
  .main-title {
    position: absolute; top: 78px; left: 0; width: 572px; text-align: center;
    font-family: "Archivo Black", Arial, sans-serif; font-size: 150px; line-height: 1; letter-spacing: -2px;
    white-space: nowrap;
  }
  .subtitle {
    position: absolute; top: 257px; left: 0; width: 572px; text-align: center;
    font-weight: 900; font-size: 30px; color: var(--heading); white-space: nowrap;
  }
  .front-strap {
    position: absolute; top: 667px; left: 0; width: 572px; text-align: center;
    font-family: "Roboto Condensed", Arial, sans-serif; font-weight: 700; font-size: 19px; color: #ffffff;
    white-space: nowrap;
  }
  .author-name {
    position: absolute; top: 702px; left: 0; width: 572px; text-align: center;
    font-family: "Archivo Black", Arial, sans-serif; font-size: 56px; letter-spacing: 4px; line-height: 1.1;
    white-space: nowrap;
  }
</style>
</head>
<body>
<main class="cover-spread">
  <section class="back-cover">
    <p class="back-quote">“You cannot rely on anyone but yourself to save your life…”</p>
    <div class="family-photo" role="img" aria-label="Photo of three family members standing together outdoors, one in a suit, one casual, one in police uniform"></div>
    <div class="photo-captions">
      <span class="caption-left">Lt. Dan Halvers</span>
      <span class="caption-mid">Marcus Halvers</span>
      <span class="caption-right">Colin Halvers</span>
    </div>

    <article class="excerpt excerpt-one">
      <h3>Dan’s Story</h3>
      <p>“And then I heard it. The unmistakable sound of a shotgun being racked. And then another one. I was hit with near-blinding light from police flashlights, but was still able to make out the silhouettes of officers taking cover behind their patrol car doors… All weapons pointed directly at me…”</p>
    </article>
    <article class="excerpt excerpt-two">
      <h3>Marcus’s Story</h3>
      <p>“Marcus stood over him, holding the shotgun in his left hand and his now empty handgun in his right. He stood there in stunned disbelief at how a routine call had escalated into a violent confrontation in a matter of seconds. The stench emanating from the house, mixed with the smell of gunpowder and blood, was almost overwhelming.”</p>
    </article>
    <article class="excerpt excerpt-three">
      <h3>Colin’s Story</h3>
      <p>“Colin desperately wanted to stay with Ray, but the danger still presented by Tillman was paramount. As Colin rushed towards the suspended vehicle, the door suddenly opened. Tillman climbed out and dropped to the ground. He stood and faced Colin like a raging bull. If the bull charged, Colin was prepared to shoot again…”</p>
    </article>
  </section>

  <section class="spine">
    <div class="spine-text">
      <span class="spine-author">DAN HALVERS</span>
      <span class="spine-title">R.K.V.</span>
      <span class="spine-subtitle">Beyond The Silence Broke</span>
    </div>
  </section>

  <section class="front-cover">
    <div class="firing-scene" role="img" aria-label="Hand firing a revolver, seen from the shooter's perspective, in blue tones"></div>
    <p class="front-tagline">It will happen, and it will come out of nowhere…</p>
    <h1 class="main-title silver-text">R.K.V.</h1>
    <h2 class="subtitle">Beyond The Silence Broke</h2>
    <p class="front-strap">One law enforcement family… three life-changing stories</p>
    <p class="author-name silver-text">DAN HALVERS</p>
  </section>
</main>
</body>
</html>
```